New Business Card Design Project

We want a modern business card that catches the attention of other remodeling companies as well as homeowners. We would like it to be informative but still simple.

Target Market(s)

Residential and other Business's

Contact Information for Business Card

TrellBrix
Phone number is 7403927048
Address is
4817 SW 3rd Lane
Marlow Springs, Ohio 44982
email is trellbrixco@quamlet.com

Requirements
Must have
• Our tagline
• Honest | Professional | Affordable

```html
<!DOCTYPE html>
<html lang="en">
<head>
<meta charset="utf-8">
<title>TrellBrix Business Card</title>
<link href="https://fonts.googleapis.com/css2?family=Oswald:wght@500&family=Raleway:wght@400;800&display=swap" rel="stylesheet">
<style>
  :root {
    --backdrop: #e0e0e0;
    --card-white: #ffffff;
    --brand-blue: #0a67cc;
    --brand-orange: #d35400;
    --ink: #3a3a3a;
    --gradient-deep: #0767c9;
    --gradient-light: #6498cf;
  }
  * { margin: 0; padding: 0; box-sizing: border-box; }
  html, body { width: 1200px; height: 1085px; overflow: hidden; }
  body { background: var(--backdrop); position: relative; font-family: "Raleway", sans-serif; }

  .card {
    position: absolute;
    left: 276px;
    width: 649px;
    height: 389px;
    box-shadow: 0 2px 6px rgba(0,0,0,0.18);
  }
  .card--front { top: 114px; background: var(--card-white); }
  .card--back {
    top: 581px;
    background: linear-gradient(45deg, var(--gradient-deep) 0%, var(--gradient-light) 100%);
  }

  .brand-name {
    position: absolute;
    left: 0; right: 0;
    text-align: center;
    font-family: "Raleway", sans-serif;
    font-weight: 800;
    line-height: 1;
    white-space: nowrap;
  }
  .card--front .brand-name {
    top: 40px; font-size: 74px; letter-spacing: 4px; padding-left: 4px;
    color: var(--brand-blue);
  }
  .card--back .brand-name {
    top: 147px; font-size: 94px; letter-spacing: 10px; padding-left: 10px;
    color: var(--card-white);
  }

  .lockup-tagline {
    position: absolute;
    left: 0; right: 0;
    text-align: center;
    font-family: "Oswald", sans-serif;
    font-weight: 500;
    text-transform: uppercase;
    line-height: 1;
    white-space: nowrap;
  }
  .card--front .lockup-tagline { top: 109px; font-size: 19px; color: var(--brand-blue); letter-spacing: 0.2px; }
  .card--front .lockup-tagline .divider { color: var(--brand-orange); }
  .card--back .lockup-tagline { top: 241px; font-size: 27px; color: var(--card-white); letter-spacing: 0.4px; }

  .contact-list {
    position: absolute;
    top: 170px;
    left: 0; right: 0;
    list-style: none;
    display: flex;
    flex-direction: column;
    align-items: center;
    gap: 17px;
    color: var(--ink);
    font-size: 19px;
  }
  .contact-item { display: flex; align-items: center; gap: 10px; height: 24px; white-space: nowrap; }
  .contact-icon { width: 20px; height: 20px; fill: var(--brand-orange); flex: none; }

  .values-line {
    position: absolute;
    top: 327px;
    left: 0; right: 0;
    text-align: center;
    font-size: 20px;
    letter-spacing: 1.5px;
    color: var(--ink);
    white-space: nowrap;
  }
  .values-line .divider { color: var(--brand-orange); margin: 0 6px; }
</style>
</head>
<body>

<section class="card card--front" aria-label="Business card front">
  <h1 class="brand-name">TrellBrix</h1>
  <p class="lockup-tagline">Honest <span class="divider">|</span> Professional <span class="divider">|</span> Affordable</p>

  <ul class="contact-list">
    <li class="contact-item">
      <svg class="contact-icon" viewBox="0 0 24 24" aria-hidden="true"><path d="M6.6 10.8c1.4 2.8 3.8 5.1 6.6 6.6l2.2-2.2c.3-.3.7-.4 1-.2 1.1.4 2.3.6 3.6.6.6 0 1 .4 1 1V20c0 .6-.4 1-1 1C10.6 21 3 13.4 3 4c0-.6.4-1 1-1h3.5c.6 0 1 .4 1 1 0 1.2.2 2.4.6 3.6.1.3 0 .7-.2 1l-2.3 2.2z"/></svg>
      <span>7403927048</span>
    </li>
    <li class="contact-item">
      <svg class="contact-icon" viewBox="0 0 24 24" aria-hidden="true"><path d="M2 5h20v14H2V5zm2 2v.3l8 5.6 8-5.6V7H4zm16 2.7l-8 5.6-8-5.6V17h16V9.7z"/></svg>
      <span>trellbrixco@quamlet.com</span>
    </li>
    <li class="contact-item">
      <svg class="contact-icon" viewBox="0 0 24 24" aria-hidden="true"><path d="M12 2C8.1 2 5 5.1 5 9c0 5.2 7 13 7 13s7-7.8 7-13c0-3.9-3.1-7-7-7zm0 9.5c-1.4 0-2.5-1.1-2.5-2.5S10.6 6.5 12 6.5s2.5 1.1 2.5 2.5-1.1 2.5-2.5 2.5z"/></svg>
      <span>4817 SW 3rd Lane Marlow Springs, Ohio 44982</span>
    </li>
  </ul>

  <p class="values-line">Honest<span class="divider">|</span>Professional<span class="divider">|</span>Affordable</p>
</section>

<section class="card card--back" aria-label="Business card back">
  <h2 class="brand-name">TrellBrix</h2>
  <p class="lockup-tagline">Honest | Professional | Affordable</p>
</section>

</body>
</html>
```